Website Design for two swimming school brands

Looking for a modern, engaging website design for my new business Every Stroke Water Learning. Within that business I have two current brands:
Every Stroke Swim and Yard Paddle
My current website (www.yardpaddle.net) has most of the info you'll need. Feel free to also use my socials for content.
Looking for someone to do the initial design/setup and then hand over full control to me with no ongoing fees or charges (except for hosting), and I'm responsible for all future changes. Ideally made and then can be edited in google sites but open to other options.

Website requirements are quite simple for both pages.
For the Yard Paddle page, I'd like the same info and features that are on my current website presented in a fresh way.
For the Every Stroke page, I'd like to see your concepts for design and possible sections, but it'll be roughly the same as the yard paddle one. I will upload a document soon for text and sections and other information to go on the Every stroke swim page.

For clarity the difference between the business' is one goes out to people's home pools and the other hires out lane space in public pool to conduct lessons.
I'd like a lighter theme for the Yard Paddle Website and a Darker one for the Every Stroke.
Both pages needs to be accessible with picture descriptions for screen reader and other similar features.

I currently use Bookora for all my inquiry, booking and payment functions so the website would need to be compatible with their widgets.

Have a look at the MockUp v2 or the business card design to get the concept of two different brandings working together.

Some text from the Every Stroke Swim Page can be found in this document:
https://docs.example-files.net/document/d/7QpaLmRvXc2TnWb8KdYs4FgHe9JuZoNi3VcXaBt/edit?usp=sharing
-
Feel free to ask any further questions.
Updates

Target Market(s)

Families and disability service providers

Industry/Entity Type

Sports and Recreation

Coding

Coded - Design and coding required

Number of Pages Required

4 page

Requirements
Must have
• Engaging design, ability to put in widgets into website, cross links between two business
Nice to have
• Common elements across the two pages but also points of difference

```html
<!DOCTYPE html>
<html lang="en">
<head>
<meta charset="utf-8">
<title>Every Stroke Swim School – Mobile Swimming Lessons</title>
<link href="https://fonts.googleapis.com/css2?family=Libre+Baskerville:wght@400;700&family=Montserrat:wght@400;500;600&display=swap" rel="stylesheet">
<style>
  :root {
    --navy: #2b3578;
    --blue: #14a2d8;
    --white: #ffffff;
    --ink: #2f3a6e;
    --hero-top: #4a9cc4;
    --hero-mid: #145477;
    --hero-deep: #05203a;
    --page: #ffffff;
  }
  * { margin: 0; padding: 0; box-sizing: border-box; }
  html, body { width: 1113px; height: 1200px; overflow: hidden; background: var(--page); }
  body { position: relative; font-family: "Montserrat", sans-serif; }
  a { text-decoration: none; }

  .hero-photo {
    position: absolute; left: 0; top: 0; width: 1113px; height: 640px;
    background:
      radial-gradient(ellipse 260px 170px at 720px 290px, rgba(222,168,118,0.45), transparent 72%),
      radial-gradient(ellipse 360px 110px at 600px 60px, rgba(150,205,230,0.35), transparent 75%),
      radial-gradient(ellipse 300px 90px at 220px 150px, rgba(110,180,215,0.25), transparent 75%),
      linear-gradient(180deg, var(--hero-top) 0%, #2a7aa4 20%, var(--hero-mid) 45%, #0a3252 65%, var(--hero-deep) 80%, #8fa0ae 92%, var(--page) 100%);
  }

  .site-header { position: absolute; left: 0; top: 0; width: 1113px; height: 90px; }
  .brand {
    position: absolute; left: 150px; top: 28px; width: 128px;
    color: var(--white); text-align: center; line-height: 1; white-space: nowrap;
  }
  .brand-mark { display: block; width: 22px; height: 22px; margin: 0 auto 10px; border: 2px solid var(--white); border-radius: 50%; }
  .brand-name { display: block; font-size: 17px; font-weight: 400; letter-spacing: 0.2px; }
  .brand-sub { display: block; font-size: 9px; font-weight: 400; margin-top: 4px; }
  .main-nav a {
    position: absolute; top: 36px; color: var(--white);
    font-size: 10.5px; font-weight: 600;
  }
  .search-icon { position: absolute; left: 936px; top: 33px; }

  .hero-copy { position: absolute; left: 155px; top: 248px; color: var(--white); font-family: "Libre Baskerville", serif; }
  .hero-kicker { font-size: 17px; letter-spacing: 3.2px; font-weight: 400; line-height: 1; }
  .hero-title { font-size: 72px; font-weight: 400; line-height: 1; margin-top: 24px; letter-spacing: -0.5px; }
  .hero-sub { font-size: 41px; font-weight: 400; line-height: 1; margin-top: 18px; }

  .about-photo-main {
    position: absolute; left: 138px; top: 634px; width: 791px; height: 378px;
    background:
      radial-gradient(ellipse 140px 190px at 640px 190px, rgba(20,40,70,0.35), transparent 75%),
      radial-gradient(ellipse 90px 170px at 520px 200px, rgba(40,110,200,0.35), transparent 75%),
      radial-gradient(ellipse 200px 120px at 120px 60px, rgba(200,240,252,0.55), transparent 75%),
      linear-gradient(120deg, #7fd3ef 0%, #3fb6e2 35%, #1ea4d6 65%, #1286bd 100%);
  }
  .about-photo-frame { position: absolute; left: 595px; top: 941px; width: 369px; height: 259px; background: var(--white); }
  .about-photo-group {
    position: absolute; left: 11px; top: 11px; width: 358px; height: 248px;
    background:
      radial-gradient(ellipse 170px 30px at 180px 150px, rgba(240,220,90,0.5), transparent 75%),
      radial-gradient(ellipse 200px 50px at 180px 105px, rgba(40,140,220,0.45), transparent 75%),
      linear-gradient(180deg, #3f7fb0 0%, #5a94bf 18%, #3aa7da 34%, #2a9bd3 100%);
  }

  .about-card {
    position: absolute; left: 174px; top: 667px; width: 341px; height: 488px;
    background: var(--white); box-shadow: 0 4px 18px rgba(20,40,80,0.12);
    padding: 44px 0 0 24px;
  }
  .about-kicker { font-family: "Libre Baskerville", serif; color: var(--blue); font-size: 17px; letter-spacing: 3px; font-weight: 400; line-height: 1; }
  .about-title { font-family: "Libre Baskerville", serif; font-size: 29px; line-height: 35px; font-weight: 400; color: var(--navy); margin-top: 10px; }
  .about-title strong { color: var(--blue); font-weight: 700; }
  .about-text { font-size: 10.8px; line-height: 19.2px; color: var(--ink); margin-top: 13px; width: 300px; }
  .about-text + .about-text { margin-top: 19px; }
  .btn-read {
    display: inline-block; margin-top: 20px; width: 117px; height: 38px; line-height: 38px;
    background: var(--blue); color: var(--white); text-align: center;
    font-family: "Libre Baskerville", serif; font-weight: 700; font-size: 14px;
  }
</style>
</head>
<body>
  <div class="hero-photo" role="img" aria-label="Smiling child in goggles swimming underwater in a blue pool"></div>

  <header class="site-header">
    <a class="brand" href="#"><span class="brand-mark"></span><span class="brand-name">EVERY STROKE</span><span class="brand-sub">Swim School</span></a>
    <nav class="main-nav">
      <a href="#" style="left:364px">Home</a>
      <a href="#" style="left:444px">About Me</a>
      <a href="#" style="left:544px">My Services</a>
      <a href="#" style="left:652px">Testimonies</a>
      <a href="#" style="left:762px">Pricing</a>
      <a href="#" style="left:848px">Links</a>
    </nav>
    <svg class="search-icon" width="22" height="22" viewBox="0 0 22 22" aria-label="Search" role="img">
      <circle cx="9" cy="9" r="7.5" fill="none" stroke="#fff" stroke-width="2"/>
      <line x1="14.5" y1="14.5" x2="20.5" y2="20.5" stroke="#fff" stroke-width="2.2" stroke-linecap="round"/>
    </svg>
  </header>

  <section class="hero-copy">
    <p class="hero-kicker">MOBILE SWIMMING LESSONS</p>
    <h1 class="hero-title">For All Ages</h1>
    <p class="hero-sub">&amp; Abilities In Adelaide</p>
  </section>

  <div class="about-photo-main" role="img" aria-label="Swim instructor supporting a child floating on their back in a pool"></div>
  <div class="about-photo-frame">
    <div class="about-photo-group" role="img" aria-label="Three children with kickboards and swim caps learning with an instructor"></div>
  </div>

  <article class="about-card">
    <p class="about-kicker">ABOUT US</p>
    <h2 class="about-title">About Swimming<br><strong>Club Service</strong></h2>
    <p class="about-text">Theo's life, from the very start, revolved around water. His parents met in a swimming club and started him swimming before he could walk! From a young age, teaching has come naturally to him and it is something that he truly enjoys.</p>
    <p class="about-text">In his spare time, he enjoys hiking with friends and playing Ultimate Frisbee, including helping to coordinate a weekly social league.</p>
    <p class="about-text">Some life highlights that paved the way for him to start offering private swimming lessons:</p>
    <a class="btn-read" href="#">Read More</a>
  </article>
</body>
</html>
```